Bright Tutor Circle business card

Use existing logo to design a business card which contains information that is listed below. Use of logo as attached. It is important that the colour scheme matches the logo already designed. It needs to be crisp and professional. This is an on line business, a database of training providers for educational establishments. The website will provide users with full information on trainers who are available and their credibility.
Target Market(s)
Educators and training providers
Industry/Entity Type
Education
Contact Information for Business Card
See below for details
Font styles to use
Colors
Designer to choose colors to be used in the design.
Requirements
Must have
- Email address mara@brighttutorcircle.co.uk
- Twitter feed. @MaraBtc
- LinkedIn details Mara Fenwick
- Mobile phone number 07812 540913
- Mission statement: To create a learning network that ensures that schools receive first class training that is excellent value for money.
Nice to have
- N/a
Should not have
- Twee educational images

```html
<!DOCTYPE html>
<html lang="en">
<head>
<meta charset="utf-8">
<title>Bright Tutor Circle – Business Card</title>
<link href="https://fonts.googleapis.com/css2?family=Montserrat:wght@400;500;600&display=swap" rel="stylesheet">
<style>
  :root {
    --page-bg: #ececec;
    --card-white: #ffffff;
    --brand-blue: #1f8ad6;
    --brand-deep: #1a6fbf;
    --sky-light: #0aa3e8;
    --sky-deep: #0a78cf;
    --ink: #1c1c1c;
    --on-blue: #ffffff;
  }
  * { box-sizing: border-box; margin: 0; padding: 0; }
  html, body {
    width: 1200px; height: 900px; overflow: hidden;
    background: var(--page-bg);
    font-family: "Montserrat", sans-serif;
  }
  .stage {
    position: relative; width: 1200px; height: 900px;
    display: flex; align-items: center; justify-content: center; gap: 60px;
  }
  .card {
    position: relative; width: 520px; height: 300px;
    border-radius: 22px; overflow: hidden;
    box-shadow: 0 14px 30px rgba(0,0,0,0.12);
  }
  /* Front */
  .card-front { background: var(--card-white); }
  .front-brand {
    position: absolute; left: 32px; top: 58px;
    display: flex; align-items: center; gap: 14px;
  }
  .brand-dot {
    width: 34px; height: 34px; border-radius: 50%;
    background: var(--brand-blue);
  }
  .brand-name {
    font-weight: 600; font-size: 28px; line-height: 1.05;
    text-transform: uppercase; color: var(--brand-blue);
    letter-spacing: 0.5px;
  }
  .front-rule {
    position: absolute; left: 0; right: 0; top: 150px;
    height: 4px; background: var(--brand-deep);
  }
  .contact-list {
    position: absolute; left: 30px; top: 180px;
    list-style: none;
  }
  .contact-item {
    display: flex; align-items: center; gap: 8px;
    font-size: 15px; font-weight: 500; color: var(--ink);
    height: 22px;
  }
  .contact-icon { width: 14px; height: 14px; flex: none; }
  .contact-icon.plain-dot {
    border-radius: 50%; background: var(--brand-deep);
  }
  /* Back */
  .card-back {
    background: linear-gradient(135deg, var(--sky-light) 0%, var(--sky-deep) 100%);
    color: var(--on-blue);
  }
  .back-texture {
    position: absolute; inset: 0;
    background: radial-gradient(ellipse at 70% 20%, rgba(255,255,255,0.14), rgba(255,255,255,0) 60%);
  }
  .back-brand {
    position: absolute; left: 0; right: 0; top: 88px;
    display: flex; align-items: center; justify-content: center; gap: 14px;
  }
  .back-brand .brand-dot { background: var(--on-blue); }
  .back-brand .brand-name { color: var(--on-blue); }
  .mission {
    position: absolute; left: 20px; right: 20px; top: 222px;
    text-align: center; text-transform: uppercase;
  }
  .mission-title {
    font-weight: 600; font-size: 11px; letter-spacing: 3px; margin-bottom: 4px;
  }
  .mission-text {
    font-size: 9.5px; letter-spacing: 1.8px; line-height: 1.45;
  }
</style>
</head>
<body>
<main class="stage">
  <section class="card card-front">
    <div class="front-brand">
      <span class="brand-dot"></span>
      <span class="brand-name">Bright Tutor<br>Circle</span>
    </div>
    <div class="front-rule"></div>
    <ul class="contact-list">
      <li class="contact-item">
        <svg class="contact-icon" viewBox="0 0 24 24"><path fill="#1a6fbf" d="M6.6 10.8a15 15 0 0 0 6.6 6.6l2.2-2.2c.3-.3.7-.4 1-.2 1.1.4 2.3.6 3.6.6.6 0 1 .4 1 1V20c0 .6-.4 1-1 1A17 17 0 0 1 3 4c0-.6.4-1 1-1h3.5c.6 0 1 .4 1 1 0 1.3.2 2.5.6 3.6.1.3 0 .7-.2 1z"/></svg>
        07812 540913
      </li>
      <li class="contact-item">
        <svg class="contact-icon" viewBox="0 0 24 24"><rect x="2" y="5" width="20" height="14" rx="1.5" fill="#1a6fbf"/><path d="M3 6l9 7 9-7" stroke="#fff" stroke-width="1.6" fill="none"/></svg>
        mara@brighttutorcircle.co.uk
      </li>
      <li class="contact-item">
        <span class="contact-icon plain-dot"></span>
        @MaraBtc
      </li>
      <li class="contact-item">
        <span class="contact-icon plain-dot"></span>
        Mara Fenwick
      </li>
    </ul>
  </section>

  <section class="card card-back">
    <div class="back-texture" role="img" aria-label="Soft pattern of overlapping translucent circles"></div>
    <div class="back-brand">
      <span class="brand-dot"></span>
      <span class="brand-name">Bright Tutor<br>Circle</span>
    </div>
    <div class="mission">
      <p class="mission-title">Mission Statement</p>
      <p class="mission-text">To create a learning network that ensures that schools receive<br>first class training that is excellent value for money.</p>
    </div>
  </section>
</main>
</body>
</html>
```